product development company PEVRANOX LLC business card

We need a business card design for a company based in Texas called 'PEVRANOX LLC'. Our first product is a illuminated portable ice chest that is called ' Ember Ridge coolers'. Ember ridge coolers is trademarked. I would like to have the ember ridge trademark somewhere on the card as well as the PEVRANOX LLC name.

Target Market(s)

outdoor industry

Industry/Entity Type

Business

Contact Information for Business Card

i would like to have PEVRANOX LLC logo larger than the Ember ridge coolers logo.

Font styles to use
Serif
Sans Serif

```html
<!DOCTYPE html>
<html lang="en">
<head>
<meta charset="utf-8">
<title>PEVRANOX LLC – Business Card</title>
<link href="https://fonts.googleapis.com/css2?family=Open+Sans:wght@400;600;700&display=swap" rel="stylesheet">
<style>
  :root {
    --backdrop: #e8e5e1;
    --card-white: #ffffff;
    --ink: #111111;
    --card-black: #050505;
    --reverse-ink: #f2f2f2;
  }
  * { margin: 0; padding: 0; box-sizing: border-box; }
  html, body {
    width: 1200px; height: 1000px; overflow: hidden;
    background: var(--backdrop);
    font-family: "Open Sans", Arial, sans-serif;
    color: var(--ink);
  }
  .canvas { position: relative; width: 1200px; height: 1000px; }

  .card {
    position: absolute; left: 265px; width: 666px; height: 397px;
    box-shadow: 0 3px 10px rgba(0,0,0,0.25);
    overflow: hidden;
  }
  .card--front { top: 73px; background: var(--card-white); }
  .card--back { top: 532px; background: var(--card-black); }

  .wordmark {
    position: absolute; text-align: center;
    font-family: "Open Sans", Arial, sans-serif; font-weight: 600;
    text-transform: uppercase; line-height: 1;
  }
  .wordmark__name { display: block; letter-spacing: 2px; }
  .wordmark__suffix { display: block; letter-spacing: 12px; margin-top: 10px; }

  .card--front .wordmark { left: 33px; top: 45px; width: 295px; color: var(--ink); }
  .card--front .wordmark__name { font-size: 42px; }
  .card--front .wordmark__suffix { font-size: 20px; }

  .card--back .wordmark { left: 0; top: 163px; width: 666px; color: var(--reverse-ink); }
  .card--back .wordmark__name { font-size: 46px; }
  .card--back .wordmark__suffix { font-size: 21px; }

  .holder { position: absolute; left: 33px; top: 182px; }
  .holder__name { font-size: 20px; font-weight: 700; line-height: 24px; }
  .holder__title { font-size: 15px; line-height: 20px; }

  .contact-list { position: absolute; left: 33px; top: 246px; list-style: none; }
  .contact-list li {
    display: flex; align-items: center; height: 23px;
    font-size: 15px; line-height: 1;
  }
  .contact-list li.contact--address { margin-top: 5px; }
  .contact-list svg { width: 16px; height: 16px; margin-right: 6px; fill: var(--ink); flex: none; }

  .product-mark {
    position: absolute; left: 452px; top: 296px;
    display: flex; align-items: center; gap: 8px;
    font-family: "Open Sans", Arial, sans-serif; font-weight: 700;
    font-size: 22px; color: var(--ink);
  }
  .product-mark__dot { width: 26px; height: 26px; border-radius: 50%; background: var(--ink); }

  .edge-band { position: absolute; left: 0; bottom: 0; width: 666px; height: 13px; }
  .edge-band polygon { fill: var(--ink); }
</style>
</head>
<body>
<div class="canvas">

  <section class="card card--front" aria-label="Business card front">
    <div class="wordmark">
      <span class="wordmark__name">Pevranox</span>
      <span class="wordmark__suffix">LLC</span>
    </div>

    <div class="holder">
      <p class="holder__name">MARCO VILLANUEVA</p>
      <p class="holder__title">Managing Director</p>
    </div>

    <ul class="contact-list">
      <li>
        <svg viewBox="0 0 16 16" aria-hidden="true"><path d="M5 1h6a1 1 0 0 1 1 1v12a1 1 0 0 1-1 1H5a1 1 0 0 1-1-1V2a1 1 0 0 1 1-1zm.5 2v8h5V3zm2.5 9.2a.9.9 0 1 0 0 1.8.9.9 0 0 0 0-1.8z"/></svg>
        + 000 000 0000
      </li>
      <li>
        <svg viewBox="0 0 16 16" aria-hidden="true"><path d="M1 6c0-2 3-3 7-3s7 1 7 3v1h-4V5.5H5V7H1zm3 2h8l2 6H2zm4 1.5a2 2 0 1 0 0 4 2 2 0 0 0 0-4z"/></svg>
        + 000 000 0000
      </li>
      <li>
        <svg viewBox="0 0 16 16" aria-hidden="true"><path d="M1 4h14v8H1zm1 1v.4l6 3.8 6-3.8V5z"/></svg>
        info@pevranoxemberridge.com
      </li>
      <li>
        <svg viewBox="0 0 16 16" aria-hidden="true"><path d="M8 1a7 7 0 1 0 0 14A7 7 0 0 0 8 1zm0 1.5c.8 0 1.7 1.6 2 4H6c.3-2.4 1.2-4 2-4zM2.6 7.5h2.3c0 .3 0 .7.1 1H2.6a5.6 5.6 0 0 1 0-1zm8.5 0h2.3a5.6 5.6 0 0 1 0 1h-2.3zM6 9.5h4c-.3 2.4-1.2 4-2 4s-1.7-1.6-2-4z"/></svg>
        www.pevranoxemberridge.com
      </li>
      <li class="contact--address">
        <svg viewBox="0 0 16 16" aria-hidden="true"><path d="M8 0a5.5 5.5 0 0 0-5.5 5.5C2.5 10 8 16 8 16s5.5-6 5.5-10.5A5.5 5.5 0 0 0 8 0zm0 3.3a2.2 2.2 0 1 1 0 4.4 2.2 2.2 0 0 1 0-4.4z"/></svg>
        1840 W. Mesa Rd. Alton, TX 78573
      </li>
    </ul>

    <div class="product-mark">
      <span class="product-mark__dot" aria-hidden="true"></span>
      <span>Ember Ridge</span>
    </div>

    <svg class="edge-band" viewBox="0 0 666 13" preserveAspectRatio="none" aria-hidden="true">
      <polygon points="0,0 358,0 378,13 0,13"/>
      <polygon points="388,6 666,6 666,13 392,13"/>
    </svg>
  </section>

  <section class="card card--back" aria-label="Business card back">
    <div class="wordmark">
      <span class="wordmark__name">Pevranox</span>
      <span class="wordmark__suffix">LLC</span>
    </div>
  </section>

</div>
</body>
</html>
```